2 x storefront vinyl request

We are transitioning to a storefront office and need two vinyls for the windows.

First vinyl: Use the Aldwick Partners logo, website (www.aldwickpartnersestates.example) and leasing office number ((555) 318-4726)

Second vinyl: Maintenance Division & phone number (555) 318-4726

```html
<!DOCTYPE html>
<html lang="en">
<head>
<meta charset="utf-8">
<title>Aldwick Partners – Storefront Vinyls</title>
<link rel="stylesheet" href="https://fonts.googleapis.com/css2?family=Oswald:wght@600&family=Rubik:wght@600;700&display=swap">
<style>
  :root{
    --page:#e3e1e2;
    --slate:#555b5b;
    --ink:#0d0d0d;
    --rule-grey:#a6aaa8;
    --paper:#ffffff;
    --logo-grey:#4f5454;
    --label-top:#7a7a7a;
  }
  *{margin:0;padding:0;box-sizing:border-box}
  html,body{width:1200px;height:2435px;overflow:hidden;background:var(--page)}
  .sheet{position:relative;width:1200px;height:2435px;display:flex;justify-content:center;align-items:center;gap:60px}
  .vinyl{position:relative;width:540px;height:1080px;overflow:hidden;box-shadow:0 4px 14px rgba(0,0,0,.18)}
  .vinyl-art{position:absolute;inset:0;width:100%;height:100%}
  .brand-name{position:absolute;left:0;right:0;top:340px;text-align:center;
    font-family:"Rubik",sans-serif;font-weight:700;font-size:38px;line-height:1.05;
    color:var(--logo-grey);text-transform:uppercase;letter-spacing:.5px}
  .label{position:absolute;left:43px;width:452px;border-radius:9px;
    background:linear-gradient(180deg,var(--label-top) 0%,#2a2a2a 55%,var(--ink) 100%);
    color:var(--paper);font-family:"Rubik",sans-serif;font-weight:600;text-align:center}
  .label::after{content:"";position:absolute;left:50%;bottom:-20px;margin-left:-12px;
    border-left:12px solid transparent;border-right:12px solid transparent;border-top:20px solid var(--ink)}
  .label--single{top:632px;height:80px;font-size:50px;line-height:78px}
  .label--double{top:632px;height:130px;font-size:48px;line-height:58px;padding-top:6px}
  .phone{position:absolute;left:43px;display:flex;align-items:center;gap:22px}
  .phone--leasing{top:740px}
  .phone--maintenance{top:790px}
  .phone-icon{width:66px;height:66px;flex:none}
  .phone-number{font-family:"Oswald",sans-serif;font-weight:600;font-size:62px;color:#222;letter-spacing:1px;line-height:1}
  .website{position:absolute;left:0;right:0;bottom:80px;text-align:center;
    font-family:"Oswald",sans-serif;font-weight:600;font-size:24px;color:var(--paper);letter-spacing:.3px}
</style>
</head>
<body>
<main class="sheet">

  <section class="vinyl vinyl--leasing">
    <svg class="vinyl-art" viewBox="0 0 500 1000" preserveAspectRatio="none" aria-hidden="true">
      <defs>
        <linearGradient id="footGradA" x1="0" y1="0" x2="0" y2="1">
          <stop offset="0" stop-color="#3a3a3a"/><stop offset="1" stop-color="#0d0d0d"/>
        </linearGradient>
      </defs>
      <rect width="500" height="1000" fill="#555b5b"/>
      <polygon points="0,265 230,72 500,262 500,790 0,790" fill="#ffffff"/>
      <line x1="12" y1="250" x2="215" y2="88" stroke="#0d0d0d" stroke-width="28" stroke-linecap="round"/>
      <line x1="205" y1="22" x2="500" y2="250" stroke="#a6aaa8" stroke-width="16"/>
      <line x1="222" y1="4" x2="500" y2="218" stroke="#0d0d0d" stroke-width="26" stroke-linecap="round"/>
      <path d="M0,615 Q0,600 22,600 L22,790 L0,790 Z" fill="#0d0d0d"/>
      <rect y="790" width="500" height="38" fill="#0d0d0d"/>
      <rect y="828" width="500" height="20" fill="#a6aaa8"/>
      <rect y="848" width="500" height="152" fill="url(#footGradA)"/>
    </svg>
    <p class="brand-name">Aldwick<br>Partners<br>Properties</p>
    <div class="label label--single">leasing office</div>
    <div class="phone phone--leasing">
      <svg class="phone-icon" viewBox="0 0 66 66" aria-hidden="true">
        <circle cx="33" cy="33" r="32" fill="#0d0d0d"/>
        <path d="M24 19c2-1 4 0 5 2l2 5c1 2 0 3-1 4l-2 2c2 4 5 7 9 9l2-2c1-1 2-2 4-1l5 2c2 1 3 3 2 5l-1 3c-1 2-3 3-5 3-12-1-23-12-24-24 0-2 1-4 3-5z" fill="#ffffff"/>
      </svg>
      <span class="phone-number">(555) 318-4726</span>
    </div>
    <p class="website">WWW.ALDWICKPARTNERSESTATES.EXAMPLE</p>
  </section>

  <section class="vinyl vinyl--maintenance">
    <svg class="vinyl-art" viewBox="0 0 500 1000" preserveAspectRatio="none" aria-hidden="true">
      <defs>
        <linearGradient id="footGradB" x1="0" y1="0" x2="0" y2="1">
          <stop offset="0" stop-color="#3a3a3a"/><stop offset="1" stop-color="#0d0d0d"/>
        </linearGradient>
      </defs>
      <rect width="500" height="1000" fill="#555b5b"/>
      <polygon points="0,265 230,72 500,262 500,815 0,815" fill="#ffffff"/>
      <line x1="12" y1="250" x2="215" y2="88" stroke="#0d0d0d" stroke-width="28" stroke-linecap="round"/>
      <line x1="205" y1="22" x2="500" y2="250" stroke="#a6aaa8" stroke-width="16"/>
      <line x1="222" y1="4" x2="500" y2="218" stroke="#0d0d0d" stroke-width="26" stroke-linecap="round"/>
      <path d="M0,655 Q0,640 22,640 L22,815 L0,815 Z" fill="#0d0d0d"/>
      <rect y="815" width="500" height="30" fill="#0d0d0d"/>
      <rect y="845" width="500" height="18" fill="#a6aaa8"/>
      <rect y="863" width="500" height="137" fill="url(#footGradB)"/>
    </svg>
    <p class="brand-name">Aldwick<br>Partners<br>Properties</p>
    <div class="label label--double">Maintenance<br>Division</div>
    <div class="phone phone--maintenance">
      <svg class="phone-icon" viewBox="0 0 66 66" aria-hidden="true">
        <circle cx="33" cy="33" r="32" fill="#0d0d0d"/>
        <path d="M24 19c2-1 4 0 5 2l2 5c1 2 0 3-1 4l-2 2c2 4 5 7 9 9l2-2c1-1 2-2 4-1l5 2c2 1 3 3 2 5l-1 3c-1 2-3 3-5 3-12-1-23-12-24-24 0-2 1-4 3-5z" fill="#ffffff"/>
      </svg>
      <span class="phone-number">(555) 318-4726</span>
    </div>
    <p class="website">WWW.ALDWICKPARTNERSESTATES.EXAMPLE</p>
  </section>

</main>
</body>
</html>
```